Standout Business Card for Recruiting New Hires

JOIN A WINNING TEAM! We are a nationally recognized Top Contractor for Paving and Parking Lot Maintenance. Our people are our most valuable asset, helping us to achieve Our Vision of building the best commercial pavement services company to benefit the best owners, the best employees and the best customers.

We want to create a Business Card to help us capture potential new hires, whenever and wherever they are discovered. This is not a traditional business card with someone's name it, only our Company Name and the information provided below.

Target Market(s)

Exceptional, standout, customer service oriented employees currently working elsewhere...at our competitors, at the car wash, in the deli, at the restaurant, in an airport, driving an Tripzel...wherever we find them.

Industry/Entity Type

Construction Company

Contact Information for Business Card

A double sided business card, with the standout feature being "Join A Winning Team" and the benefits listed somewhere on the card.

Requirements
Must have
• -Call to Action (Join a Winning Team)
• -Our Logo
• -Our Physical Address (17B Harrow Court, Clinton, CT 06287)
• -Our Website (www.BrightfieldSurfacing.com)
• -Our Phone Number (860) 555-0147.
• -Our Bullet Points (can be altered):
• - Competitive Pay
• - Full Time, Consistent Work Schedule
• - Paid Overtime / Drive Time
• - Work with Great People in a Great Environment
• - Training Program
• Something like that.
Nice to have
• Maybe it could say, "Come and Join Connecticut's Top Rated Paving Contractor" or Come grow with us. Something like that.
Should not have
• Anyone's name on it. This is a generic card for anyone at the company to give to a potential employee! (I have attached a business card sample, just to illustrate our look and feel).

```html
<!DOCTYPE html>
<html lang="en">
<head>
<meta charset="utf-8">
<title>Brightfield Surfacing – Recruiting Business Card</title>
<link href="https://fonts.googleapis.com/css2?family=Open+Sans:wght@400;600;700;800&display=swap" rel="stylesheet">
<style>
  :root {
    --ink: #0b0b0b;
    --paper: #ffffff;
    --brand-red: #d12a30;
    --stage: #e6e6e6;
    --muted: #1d1d1d;
  }
  * { margin: 0; padding: 0; box-sizing: border-box; }
  html, body { width: 1200px; height: 900px; overflow: hidden; }
  body {
    background: var(--stage);
    font-family: "Open Sans", Arial, sans-serif;
    position: relative;
  }
  .card {
    position: absolute;
    width: 600px;
    height: 343px;
    border-radius: 26px;
    overflow: hidden;
    box-shadow: 0 10px 28px rgba(0,0,0,0.25);
  }
  .card-back { left: 60px; top: 90px; background: var(--ink); color: var(--paper); }
  .card-front { left: 540px; top: 467px; background: var(--paper); color: var(--ink); }

  .card-shapes { position: absolute; inset: 0; width: 600px; height: 343px; }

  .brand {
    position: absolute;
    left: 36px;
    top: 60px;
    display: flex;
    align-items: center;
    gap: 10px;
  }
  .brand-dot { width: 30px; height: 30px; border-radius: 50%; background: var(--brand-red); flex: none; }
  .brand-name { font-weight: 800; font-size: 30px; letter-spacing: -0.5px; line-height: 1; }
  .card-back .brand-name { color: var(--paper); }
  .card-front .brand-name { color: var(--ink); }

  .tagline {
    position: absolute;
    left: 36px;
    top: 116px;
    font-size: 12.5px;
    font-weight: 600;
    letter-spacing: 0.6px;
    text-transform: uppercase;
  }

  .services {
    position: absolute;
    right: 34px;
    top: 150px;
    text-align: right;
  }
  .services-title {
    color: var(--brand-red);
    font-size: 14px;
    font-weight: 600;
    letter-spacing: 0.5px;
    margin-right: 17px;
    margin-bottom: 2px;
  }
  .services-list { list-style: none; }
  .services-list li {
    font-size: 13px;
    line-height: 18px;
    display: flex;
    justify-content: flex-end;
    align-items: center;
    gap: 10px;
  }
  .services-list li::after {
    content: "";
    width: 7px; height: 7px;
    border-radius: 50%;
    background: var(--brand-red);
    flex: none;
  }

  .cta {
    position: absolute;
    right: 16px;
    top: 240px;
    color: var(--paper);
    font-size: 12.5px;
    font-weight: 600;
    letter-spacing: 0.6px;
    text-transform: uppercase;
  }

  .contact-rule {
    position: absolute;
    left: 36px;
    top: 206px;
    width: 390px;
    height: 1.5px;
    background: var(--muted);
  }
  .contact {
    position: absolute;
    left: 44px;
    top: 214px;
    list-style: none;
    font-size: 12.5px;
    line-height: 16px;
  }
  .contact li { display: flex; align-items: center; gap: 8px; }
  .contact svg { width: 10px; height: 10px; flex: none; fill: var(--brand-red); }
  .contact .no-icon { padding-left: 18px; }
</style>
</head>
<body>

  <section class="card card-back" aria-label="Card back: recruiting benefits">
    <svg class="card-shapes" viewBox="0 0 600 343" aria-hidden="true">
      <polygon points="0,302 248,302 282,343 0,343" fill="#ffffff"/>
      <polygon points="262,314 600,292 600,301 270,323" fill="#d12a30"/>
    </svg>

    <div class="brand">
      <span class="brand-dot"></span>
      <span class="brand-name">Brightfield Surfacing</span>
    </div>

    <p class="tagline">Come and join Connecticut's top rated paving contractor</p>

    <div class="services">
      <p class="services-title">SERVICES</p>
      <ul class="services-list">
        <li>Competitive Pay</li>
        <li>Full Time, Consistent Work Schedule</li>
        <li>Paid Overtime / Drive Time</li>
        <li>Work with Great People in a Great Environment</li>
        <li>Training Program</li>
      </ul>
    </div>
  </section>

  <section class="card card-front" aria-label="Card front: contact details">
    <svg class="card-shapes" viewBox="0 0 600 343" aria-hidden="true">
      <polygon points="428,232 600,232 600,266 418,266" fill="#0b0b0b"/>
      <polygon points="0,326 400,326 418,266 430,266 410,334 0,334" fill="#d12a30"/>
    </svg>

    <div class="brand">
      <span class="brand-dot"></span>
      <span class="brand-name">Brightfield Surfacing</span>
    </div>

    <p class="cta">Join a winning team</p>

    <div class="contact-rule"></div>
    <ul class="contact">
      <li>
        <svg viewBox="0 0 10 10"><path d="M2 0.5 L3.6 2.6 L2.8 3.6 Q4 6 6.4 7.2 L7.4 6.4 L9.5 8 L8.4 9.5 Q2.5 8.6 0.5 1.6 Z"/></svg>
        (860) 555-0147
      </li>
      <li>
        <svg viewBox="0 0 10 10"><rect x="2.5" y="0.5" width="5" height="3"/><rect x="0.5" y="3.5" width="9" height="4" rx="1"/><rect x="2.5" y="6.5" width="5" height="3"/></svg>
        860.555.0182
      </li>
      <li>
        <svg viewBox="0 0 10 10"><path d="M2.5 0.5 H7.5 V9.5 H2.5 Z M3.5 1.5 V7.5 H6.5 V1.5 Z"/></svg>
        203.555.0163
      </li>
      <li>
        <svg viewBox="0 0 10 10"><path d="M0.5 2 H9.5 V8.5 H0.5 Z M1.5 3 V7.5 H8.5 V3 L5 5.6 Z M2.2 3 L5 5 L7.8 3 Z"/></svg>
        careers@brightfieldsurfacing.com
      </li>
      <li>
        <svg viewBox="0 0 10 10"><circle cx="5" cy="5" r="4.5"/></svg>
        www.BrightfieldSurfacing.com
      </li>
      <li class="no-icon">17B Harrow Court Clinton, CT 06287</li>
    </ul>
  </section>

</body>
</html>
```